Bluegum Vehicle Hire - The only locally owned company in Central Australia!

We offer 2WD hires
- Small
- Medium
- Large

We offer 4WD hires
- Utes
- Troop Carriers
- Wagons

Servicing Tourism & Mining
Camping packages available
Unlimited kilometer options available

14 Wattle Pde Alice Springs
Contact: 08 8461 3275
www.bluegumvehiclehire.com.au
info@bluegumvehiclehire.com.au

Target Market(s)

Tourism

Industry/Entity Type

Tourism

Contact Information for Business Card

Bluegum Vehicle Hire
The only locally owned company in Central Australia
14 Wattle Parade
Alice Springs NT 0870
Tel: 08 8461 3275
Fax: 08 8467 2914
Miriam Halvorsen
Tobias Halvorsen
We service the tourism industry

Font styles to use
Sans Serif

Colors
0455a3
f37122
9bcb3c

Requirements
Must have
• Name of owners
Nice to have
• Would like to see the company logo appear in green (open to suggestions)
• Pamphlet font information in white. Need a vehicle used to promote our company
Should not have
• should not have any photo's of national icons like Uluru, Kings Canyon

```html
<!DOCTYPE html>
<html lang="en">
<head>
<meta charset="utf-8">
<title>Bluegum Vehicle Hire – DL Flyers</title>
<link rel="stylesheet" href="https://fonts.googleapis.com/css2?family=Exo+2:ital,wght@0,300;0,400;0,500;0,600;0,700;1,600;1,700&display=swap">
<style>
  :root{
    --navy:#241f63;
    --orange:#f37122;
    --orange-dark:#e0601a;
    --white:#ffffff;
    --bg:#d6d6d6;
  }
  *{box-sizing:border-box;margin:0;padding:0}
  html,body{width:1200px;height:1200px;overflow:hidden}
  body{background:var(--bg);font-family:"Exo 2",sans-serif;position:relative}
  .flyer{position:absolute;top:106px;width:440px;height:988px;overflow:hidden;box-shadow:0 6px 18px rgba(0,0,0,.25)}
  .flyer--fleet{left:155px;background:var(--white)}
  .flyer--extras{left:605px;background:var(--navy)}
  .abs{position:absolute}
  .shape{position:absolute;left:0;width:440px}
  .photo{position:absolute}

  /* fleet flyer */
  .brand{left:28px;top:48px;width:175px;display:flex;align-items:center;gap:8px}
  .brand-dot{width:26px;height:26px;border-radius:50%;background:var(--orange);flex:none}
  .brand-name{font-weight:700;font-size:21px;line-height:1.05;color:var(--navy)}
  .tagline{left:215px;top:52px;font-weight:600;font-style:italic;font-size:17px;line-height:20px;color:var(--navy);white-space:nowrap}
  .photo--couple{left:0;top:120px;width:440px;height:360px;background:linear-gradient(180deg,#8fb8d8 0%,#5c8f4a 35%,#b8583a 62%,#4f7f86 100%)}
  .photo--car{border-radius:40% 40% 20% 20%/50% 50% 20% 20%;background:linear-gradient(180deg,#f3f3f3,#b9bcc0 70%,#3b3b3b)}
  .photo--suv{left:24px;top:478px;width:172px;height:96px}
  .photo--ute{left:237px;top:486px;width:180px;height:88px}
  .drive{font-weight:700;font-size:19px;color:var(--white);letter-spacing:.5px}
  .spec-list{list-style:none;color:var(--white);font-size:17px;line-height:20.5px}
  .spec-list li,.check-list li{display:flex;align-items:center;gap:6px}
  .tick{width:15px;height:15px;flex:none}
  .cater-title{left:27px;top:712px;font-weight:600;font-size:19px;letter-spacing:.8px;color:var(--navy)}
  .cater-list{left:27px;top:744px;list-style:none;color:var(--navy);font-size:19px;line-height:24px}
  .cater-list li{display:flex;align-items:flex-start;gap:8px;margin-bottom:9px}
  .cater-list .tick{margin-top:4px;width:16px;height:16px}
  .badge{left:274px;top:749px;width:146px;height:146px;border-radius:50%;background:var(--orange);border:6px solid var(--white);display:flex;flex-direction:column;align-items:center;justify-content:center;text-align:center;color:var(--navy);font-size:16px;line-height:20px}
  .badge strong{font-weight:700;font-size:19px;letter-spacing:.5px}
  .call{left:27px;top:904px;color:var(--white)}
  .call-label{font-weight:300;font-size:27px;letter-spacing:.5px;line-height:30px}
  .call-number{font-weight:500;font-size:27px;letter-spacing:.5px;line-height:30px}
  .contact{left:232px;top:906px;list-style:none;color:var(--white);font-size:11.5px;line-height:17px;font-weight:300;white-space:nowrap}
  .contact li{display:flex;align-items:center;gap:7px}
  .contact svg{width:13px;height:13px;flex:none;color:var(--orange)}
  .flyer--extras .contact svg{color:var(--white)}

  /* extras flyer */
  .photo--plain{left:0;top:0;width:440px;height:470px;background:linear-gradient(180deg,#5c93c9 0%,#a9c8e2 30%,#d9652a 42%,#c24a1c 62%,#6b6a34 76%,#3d3a22 100%)}
  .headline{left:28px;top:286px;color:var(--white);font-weight:700;font-style:italic;font-size:32px;line-height:36px;text-shadow:0 2px 4px rgba(0,0,0,.35)}
  .subline{left:28px;top:365px;color:var(--white);font-weight:600;font-style:italic;font-size:15.5px;line-height:20px;letter-spacing:.3px}
  .section-title{color:var(--orange);font-weight:700;font-style:italic;font-size:27px;line-height:30px;padding-left:16px;border-left:5px solid var(--orange)}
  .section-title--discover{left:28px;top:469px}
  .section-title--package{left:28px;top:640px}
  .check-list{list-style:none;color:var(--white)}
  .check-list--places{font-size:17px;line-height:21px}
  .check-list--places li{align-items:flex-start;margin-bottom:5px}
  .check-list--places .tick{margin-top:3px}
  .check-list--kit{font-size:13px;line-height:16px}
  .check-list--kit li{align-items:flex-start;margin-bottom:5.5px}
  .check-list--kit .tick{width:13px;height:13px;margin-top:1px}
  .note{font-size:10px;display:block}
  .note-inline{font-size:9.5px}
</style>
</head>
<body>
<svg width="0" height="0" style="position:absolute" aria-hidden="true">
  <defs>
    <symbol id="tick-orange" viewBox="0 0 20 20">
      <circle cx="9" cy="11" r="7" fill="none" stroke="#f37122" stroke-width="2.2"/>
      <path d="M5.5 10.5l3.2 3.3L18 3" fill="none" stroke="#f37122" stroke-width="2.6" stroke-linecap="round" stroke-linejoin="round"/>
    </symbol>
    <symbol id="tick-white" viewBox="0 0 20 20">
      <circle cx="9" cy="11" r="7" fill="none" stroke="#ffffff" stroke-width="2.2"/>
      <path d="M5.5 10.5l3.2 3.3L18 3" fill="none" stroke="#ffffff" stroke-width="2.6" stroke-linecap="round" stroke-linejoin="round"/>
    </symbol>
    <symbol id="icon-home" viewBox="0 0 14 14">
      <circle cx="7" cy="7" r="6.2" fill="none" stroke="currentColor" stroke-width="1.2"/>
      <path d="M3.8 7.2L7 4.3l3.2 2.9v3H3.8z" fill="currentColor"/>
    </symbol>
    <symbol id="icon-web" viewBox="0 0 14 14">
      <circle cx="7" cy="7" r="6.2" fill="none" stroke="currentColor" stroke-width="1.2"/>
      <path d="M5.2 4l4.5 3-2 .5 1.2 2.3-.9.4-1.1-2.3-1.4 1.2z" fill="currentColor"/>
    </symbol>
    <symbol id="icon-mail" viewBox="0 0 14 14">
      <circle cx="7" cy="7" r="6.2" fill="none" stroke="currentColor" stroke-width="1.2"/>
      <rect x="3.8" y="4.8" width="6.4" height="4.6" fill="none" stroke="currentColor" stroke-width="1"/>
      <path d="M3.8 4.8L7 7.4l3.2-2.6" fill="none" stroke="currentColor" stroke-width="1"/>
    </symbol>
    <symbol id="icon-person" viewBox="0 0 14 14">
      <circle cx="7" cy="7" r="6.2" fill="none" stroke="currentColor" stroke-width="1.2"/>
      <circle cx="7" cy="5.2" r="1.8" fill="currentColor"/>
      <path d="M3.9 10.4c.5-1.9 1.6-2.8 3.1-2.8s2.6.9 3.1 2.8z" fill="currentColor"/>
    </symbol>
  </defs>
</svg>

<!-- Fleet flyer -->
<section class="flyer flyer--fleet">
  <div class="photo photo--couple" role="img" aria-label="Photo of travellers beside a rental car at a palm-lined outback waterhole"></div>

  <svg class="shape" style="top:0" height="160" viewBox="0 0 440 160" aria-hidden="true">
    <path d="M0 0H440V100C330 140 200 160 0 130Z" fill="var(--white)"/>
  </svg>
  <div class="abs brand">
    <span class="brand-dot"></span>
    <span class="brand-name">Bluegum Vehicle Hire</span>
  </div>
  <p class="abs tagline">The only locally owned<br>vehicle rental company<br>in Alice Springs!</p>

  <svg class="shape" style="top:455px" height="245" viewBox="0 0 440 245" aria-hidden="true">
    <path d="M0 20C70 0 140 0 220 15C300 32 380 10 440 -5V245H0Z" fill="var(--orange)"/>
    <path d="M215 15L180 245H0V120Z" fill="var(--orange-dark)" opacity=".35"/>
    <path d="M0 232C150 190 300 195 440 215V245H0Z" fill="var(--navy)"/>
    <path d="M0 240C150 205 300 212 440 230V245H0Z" fill="var(--white)"/>
  </svg>
  <div class="photo photo--car photo--suv" role="img" aria-label="Photo of a white compact SUV"></div>
  <div class="photo photo--car photo--ute" role="img" aria-label="Photo of a white dual-cab 4WD ute"></div>

  <span class="abs drive" style="left:27px;top:604px">2WD</span>
  <ul class="abs spec-list" style="left:88px;top:588px">
    <li><svg class="tick"><use href="#tick-white"/></svg>Small</li>
    <li><svg class="tick"><use href="#tick-white"/></svg>Medium</li>
    <li><svg class="tick"><use href="#tick-white"/></svg>Large</li>
  </ul>
  <span class="abs drive" style="left:233px;top:604px">4WD</span>
  <ul class="abs spec-list" style="left:287px;top:588px">
    <li><svg class="tick"><use href="#tick-white"/></svg>Utes</li>
    <li><svg class="tick"><use href="#tick-white"/></svg>Troop Carriers</li>
    <li><svg class="tick"><use href="#tick-white"/></svg>Wagons</li>
  </ul>

  <h2 class="abs cater-title">WE CATER FOR:</h2>
  <ul class="abs cater-list">
    <li><svg class="tick"><use href="#tick-orange"/></svg><span>The Tourism &amp; Mining<br>Industries</span></li>
    <li><svg class="tick"><use href="#tick-orange"/></svg><span>Tailor Made Camping<br>Packages</span></li>
  </ul>

  <svg class="shape" style="top:820px" height="168" viewBox="0 0 440 168" aria-hidden="true">
    <path d="M0 60C120 55 250 35 440 0V168H0Z" fill="var(--navy)"/>
    <path d="M0 50C120 50 240 30 440 -5V2C250 40 120 60 0 60Z" fill="var(--white)"/>
  </svg>
  <div class="abs badge"><strong>Unlimited</strong>Kilometer Rates<br>Available</div>

  <div class="abs call">
    <p class="call-label">CALL US AT</p>
    <p class="call-number">(08) 8461 3275</p>
  </div>
  <ul class="abs contact">
    <li><svg><use href="#icon-home"/></svg>14 Wattle Pde, Alice Springs</li>
    <li><svg><use href="#icon-web"/></svg>www.bluegumvehiclehire.com.au</li>
    <li><svg><use href="#icon-mail"/></svg>info@bluegumvehiclehire.com.au</li>
    <li><svg><use href="#icon-person"/></svg>Miriam &amp; Tobias Halvorsen</li>
  </ul>
</section>

<!-- Extras flyer -->
<section class="flyer flyer--extras">
  <div class="photo photo--plain" role="img" aria-label="Photo of red outback desert plains with green scrub under a blue sky"></div>
  <svg class="shape" style="top:400px" height="80" viewBox="0 0 440 80" aria-hidden="true">
    <path d="M0 35C150 75 300 50 440 0V80H0Z" fill="var(--navy)"/>
  </svg>

  <h1 class="abs headline">Outback Camp ‘N’ Drive...<br>The Extras....</h1>
  <p class="abs subline">Bluegum Vehicle Hire provide fully equipped<br>vehicles for touring and camping</p>

  <h2 class="abs section-title section-title--discover">DISCOVER &amp; EXPLORE...</h2>
  <ul class="abs check-list check-list--places" style="left:28px;top:521px">
    <li><svg class="tick"><use href="#tick-white"/></svg><span>Ormiston Gorge &amp;<br>Glen Helen</span></li>
    <li><svg class="tick"><use href="#tick-white"/></svg>Ruby Gap</li>
    <li><svg class="tick"><use href="#tick-white"/></svg>Palm Valley</li>
  </ul>
  <ul class="abs check-list check-list--places" style="left:240px;top:521px">
    <li><svg class="tick"><use href="#tick-white"/></svg>Coober Pedy</li>
    <li><svg class="tick"><use href="#tick-white"/></svg>Rainbow Valley</li>
    <li><svg class="tick"><use href="#tick-white"/></svg>Chambers Pillar</li>
    <li><svg class="tick"><use href="#tick-white"/></svg>McDonnell Ranges</li>
  </ul>

  <h2 class="abs section-title section-title--package">CAMP ‘N’ DRIVE PACKAGE<br>INCLUDES...</h2>
  <ul class="abs check-list check-list--kit" style="left:28px;top:712px">
    <li><svg class="tick"><use href="#tick-white"/></svg><span>Unlimited Kilometers<span class="note">(Optional)</span></span></li>
    <li><svg class="tick"><use href="#tick-white"/></svg><span>Swags <span class="note-inline">(Aussie bush beds)</span></span></li>
    <li><svg class="tick"><use href="#tick-white"/></svg>BBQ</li>
    <li><svg class="tick"><use href="#tick-white"/></svg>Sleeping Bags</li>
    <li><svg class="tick"><use href="#tick-white"/></svg>Ground Sheet</li>
    <li><svg class="tick"><use href="#tick-white"/></svg>Table &amp; Chairs</li>
  </ul>
  <ul class="abs check-list check-list--kit" style="left:232px;top:712px">
    <li><svg class="tick"><use href="#tick-white"/></svg>Lantern &amp; Maps</li>
    <li><svg class="tick"><use href="#tick-white"/></svg>Water container</li>
    <li><svg class="tick"><use href="#tick-white"/></svg>Esky (Ice Cooler)</li>
    <li><svg class="tick"><use href="#tick-white"/></svg>All camping Equipment</li>
    <li><svg class="tick"><use href="#tick-white"/></svg>Full Cooking &amp; Cutlery Set</li>
  </ul>

  <svg class="shape" style="top:820px" height="168" viewBox="0 0 440 168" aria-hidden="true">
    <path d="M0 40C150 70 300 30 440 22V168H0Z" fill="var(--orange)"/>
    <path d="M0 40C150 70 300 30 440 22V10C300 12 150 55 0 30Z" fill="var(--white)"/>
  </svg>

  <div class="abs call">
    <p class="call-label">CALL US AT</p>
    <p class="call-number">(08) 8461 3275</p>
  </div>
  <ul class="abs contact">
    <li><svg><use href="#icon-home"/></svg>14 Wattle Pde, Alice Springs</li>
    <li><svg><use href="#icon-web"/></svg>www.bluegumvehiclehire.com.au</li>
    <li><svg><use href="#icon-mail"/></svg>info@bluegumvehiclehire.com.au</li>
    <li><svg><use href="#icon-person"/></svg>Miriam &amp; Tobias Halvorsen</li>
  </ul>
</section>
</body>
</html>
```